I need a great design for my Ebook because that will help spread the message

Hey there,

I wrote an eBook (THE MORNING LANTERN METHOD) about how confidence impacts one's life, why it’s important and how to get more of it and I need someone to design it nicely.

My target audience is made up of more women than men.

I have pictures for each one of the 7 steps in the book, but I am open to your suggestions.

I really like Optima as a font. I have a bit of gold in the text. I would be happy if you could keep it. You can format the text as you think best.

I'd love a modern design.

I added an old design of the ebook for you to see the way the pictures are used for each step because I want to keep that blend between the picture and the title of the step.
I like the idea of each step starting on a new page and the block footer - just not black.

I want the subtitle of each step to be a different font to the title.

Please ask any questions you have.

Thank you!

Target Market(s)

Men and women aged 25-45.

Industry/Entity Type

Life Coaching

Font styles to use
Sans Serif

Colors
ffffff

Requirements
Must have
• My brand colours only:
• navy #233264
• white
• light pink #fff3f1
• mustard yellow #ffc800.
Nice to have
• The pictures I uploaded for each step.
Should not have
• Should not have much black.

```html
<!DOCTYPE html>
<html lang="en">
<head>
<meta charset="utf-8">
<title>The Morning Lantern Method — eBook Cover</title>
<link rel="stylesheet" href="https://fonts.googleapis.com/css2?family=Bebas+Neue&family=Josefin+Sans:wght@300&family=Lato:wght@400&family=Marcellus&display=swap">
<style>
  :root {
    --navy: #233264;
    --white: #ffffff;
    --mustard: #ffc800;
    --sky: #7fd3e6;
  }
  * { margin: 0; padding: 0; box-sizing: border-box; }
  html, body {
    width: 927px;
    height: 1200px;
    overflow: hidden;
    background: var(--white);
  }
  .cover {
    position: relative;
    width: 927px;
    height: 1200px;
    overflow: hidden;
    background: var(--white);
  }
  .navy-field {
    position: absolute;
    left: 0;
    top: 394px;
    width: 927px;
    height: 806px;
    background: var(--navy);
  }
  .author-band {
    position: absolute;
    left: 71px;
    top: 500px;
    width: 294px;
    height: 700px;
    background: var(--white);
  }
  .title { font-weight: normal; }
  .title-line {
    position: absolute;
    left: 68px;
    font-family: "Bebas Neue", "Oswald", sans-serif;
    font-size: 140px;
    line-height: 140px;
    color: var(--navy);
    white-space: nowrap;
  }
  .title-line--1 { top: 45px; }
  .title-line--2 { top: 158px; }
  .title-line--3 { top: 271px; }
  .title-line--4 { top: 384px; color: var(--white); }
  .year {
    position: absolute;
    left: 803px;
    top: 60px;
    font-family: "Marcellus", serif;
    font-size: 27px;
    color: var(--navy);
  }
  .author {
    position: absolute;
    left: 227px;
    top: 848px;
    transform: translate(-50%, -50%) rotate(-90deg);
    font-family: "Josefin Sans", sans-serif;
    font-weight: 300;
    font-size: 46px;
    line-height: 1;
    letter-spacing: 17px;
    padding-left: 17px;
    color: var(--navy);
    white-space: nowrap;
  }
  .step-count {
    position: absolute;
    left: 406px;
    top: 445px;
    font-family: "Bebas Neue", sans-serif;
    font-size: 480px;
    line-height: 1;
    color: var(--mustard);
    text-shadow: 6px 6px 0 var(--sky);
    transform: scaleX(1.32);
    transform-origin: left top;
  }
  .tagline {
    position: absolute;
    left: 401px;
    top: 850px;
    font-family: "Lato", sans-serif;
    font-size: 35px;
    line-height: 38px;
    color: var(--white);
    white-space: nowrap;
  }
  .blurb {
    position: absolute;
    left: 401px;
    top: 1110px;
    font-family: "Lato", sans-serif;
    font-size: 22px;
    line-height: 23px;
    color: var(--white);
    white-space: nowrap;
  }
</style>
</head>
<body>
  <main class="cover">
    <div class="navy-field"></div>
    <div class="author-band"></div>

    <h1 class="title">
      <span class="title-line title-line--1">THE</span>
      <span class="title-line title-line--2">MORNING</span>
      <span class="title-line title-line--3">LANTERN</span>
      <span class="title-line title-line--4">METHOD</span>
    </h1>

    <p class="year">2018</p>

    <p class="author">MARENELLWOOD</p>

    <p class="step-count">7</p>

    <p class="tagline">Steps to becoming the YOU<br>who achieves their goals,<br>feels fulfilled and loves their life</p>

    <p class="blurb">Learn how confidence impacts your life,<br>why it’s important and how to get more of it</p>
  </main>
</body>
</html>
```